Tavorly - Landing Page

Need a landing page for a journal app. The app is based on a retrospective board, where each journal entry is split into 3 sections: "What went well", "What Didn't Go Well" and "Things To Try".
The landing page should match the style of all modern web application landing pages. Think Brimo, Quenta, Vexadro. I've included screenshots of the app.
One feature that I want to highlight that is not ready yet, is an AI coach. It will offer insights based on the history of the user's journal entries
1 page

```html
<!DOCTYPE html>
<html lang="en">
<head>
<meta charset="utf-8">
<title>Tavorly – Structured Journaling</title>
<link href="https://fonts.googleapis.com/css2?family=Outfit:wght@300;400;500;600;700;800&display=swap" rel="stylesheet">
<style>
:root{
  --ink:#111827;
  --text:#3b3f4a;
  --muted:#8a8f9c;
  --blue:#2f7ff5;
  --red:#e8473b;
  --green:#1fae6a;
  --yellow:#f6d21b;
  --lav:#f6f3fb;
  --line:#e8e9ef;
  --white:#ffffff;
}
*{box-sizing:border-box;margin:0;padding:0}
html,body{width:1200px;height:4255px;overflow:hidden}
body{
  font-family:"Outfit",sans-serif;color:var(--ink);position:relative;
  background:
    radial-gradient(600px 400px at 1100px 60px,#eaf1ff 0%,transparent 70%),
    radial-gradient(500px 400px at 80px 300px,#f7efff 0%,transparent 70%),
    radial-gradient(700px 500px at 1000px 1300px,#fff8e6 0%,transparent 70%),
    radial-gradient(700px 600px at 100px 2500px,#fff9e8 0%,transparent 70%),
    radial-gradient(600px 500px at 1100px 2600px,#eefaf3 0%,transparent 70%),
    #fdfdff;
}
.abs{position:absolute}
a{color:inherit;text-decoration:none}
.mark{position:relative;display:inline-block;z-index:0}
.mark::after{content:"";position:absolute;left:-4px;right:-6px;bottom:2px;height:9px;border-radius:6px;transform:rotate(-1.5deg);z-index:-1}
.mark.y::after{background:var(--yellow)}
.mark.b::after{background:var(--blue);height:6px}
.mark.g::after{background:var(--green);height:6px}
.mark.r::after{background:var(--red);height:4px}
.mark.circ::after{background:none;border:3px solid var(--blue);height:40px;bottom:-6px;border-radius:50%;transform:rotate(-4deg)}

/* nav */
.logo{font-weight:800;font-size:21px;letter-spacing:.5px}
.nav-link{font-size:11.5px;color:#555a66;top:30px}
.btn-dark{background:var(--ink);color:#fff;border-radius:6px;font-size:11.5px;font-weight:600;display:flex;align-items:center;justify-content:center}

/* hero */
.hero-title{left:0;width:1200px;top:102px;text-align:center;font-weight:800;font-size:55px;line-height:72px}
.hero-sub{left:0;width:1200px;top:262px;text-align:center;font-size:12.5px;line-height:19px;color:var(--text)}
.btn-outline{left:537px;top:315px;width:122px;height:36px;border:1.5px solid var(--ink);border-radius:6px;font-size:11.5px;font-weight:600;display:flex;align-items:center;justify-content:center;background:#fff}

/* dashboard */
.dash{left:183px;top:379px;width:834px;height:461px;background:#fff;border-radius:10px;box-shadow:0 10px 40px rgba(60,70,120,.08);overflow:hidden}
.dash-side{left:0;top:0;width:186px;height:100%}
.dash-side .logo{position:absolute;left:25px;top:24px;font-size:22px}
.side-item{position:absolute;left:15px;font-size:12px;color:#8a8f9c;display:flex;align-items:center;gap:8px}
.side-item i{width:12px;height:12px;border:1.5px solid #a0a4ae;border-radius:2px;display:block}
.side-active{position:absolute;left:0;top:69px;width:186px;height:30px;background:var(--blue);color:#fff;font-size:12px;display:flex;align-items:center;padding-left:15px;gap:8px}
.side-active i{width:12px;height:12px;border:1.5px solid #fff;border-radius:2px;display:block}
.logout{position:absolute;left:15px;top:420px;font-size:12px;color:var(--blue);display:flex;align-items:center;gap:10px}
.dash-hello{left:219px;top:29px;font-size:11px}
.dash-welcome{left:219px;top:55px;font-size:21px;font-weight:600}
.bell{left:786px;top:30px;width:36px;height:36px;border:1.5px solid var(--blue);border-radius:50%;display:flex;align-items:center;justify-content:center}
.dash-panel{left:199px;top:101px;width:623px;height:352px;background:var(--lav);border-radius:10px}
.jcard{top:26px;width:133px;height:132px;background:#fff;border:1.5px solid #dfe3f5;border-radius:8px;text-align:center}
.jcard .ic{width:54px;height:54px;border-radius:50%;margin:16px auto 0}
.jcard span{display:block;margin-top:24px;font-size:12.5px}
.btn-create{left:20px;top:182px;width:122px;height:37px;font-size:11px}
.entry{top:238px;width:261px;height:120px;background:#fff;border-radius:8px;padding:10px 10px;font-size:8.5px;line-height:12px;color:#555;overflow:hidden}
.entry b{display:block;font-size:10px;color:var(--ink);font-weight:600;margin-bottom:2px}
.entry .tag{color:#9aa0ab}

/* section heads */
.sec-title{left:0;width:1200px;text-align:center;font-weight:700;font-size:33px;line-height:44px}
.sec-desc{left:0;width:1200px;text-align:center;font-size:11.5px;line-height:18px;color:var(--text)}
.red{color:var(--red)}
.blue{color:var(--blue)}

/* feature rows */
.eyebrow{font-size:9.5px}
.feat-h{font-size:22px;font-weight:600}
.para{width:380px;font-size:12px;line-height:16.6px;color:var(--text)}
.kf{font-size:19px;font-weight:400}
.checks{list-style:none;width:380px}
.checks li{position:relative;padding-left:27px;font-size:13.5px;line-height:22px;margin-bottom:19px;color:var(--ink)}
.checks li::before{content:"";position:absolute;left:3px;top:5px;width:10px;height:5px;border-left:1.5px solid var(--ink);border-bottom:1.5px solid var(--ink);transform:rotate(-45deg)}
.checks.bl li::before{border-color:var(--blue)}
.art{border-radius:12px}
.mini{background:#fff;border-radius:6px;box-shadow:0 6px 24px rgba(30,40,80,.12);padding:10px;font-size:7.5px;line-height:10px;color:#444;overflow:hidden}
.mini .hd{font-size:7px;color:#333;margin-bottom:8px;display:flex;align-items:center;gap:4px}
.mini .hd::before{content:"";width:6px;height:6px;border-radius:50%;background:var(--blue)}
.mini .ed{border:1px solid #e5e6ea;border-radius:3px;height:calc(100% - 22px);padding:5px;overflow:hidden}
.mini .tb{height:14px;border-bottom:1px solid #e5e6ea;margin:-5px -5px 5px;padding:3px 5px;font-size:6px;color:#666;letter-spacing:2px}

/* testimonials */
.tcard{top:2645px;width:304px;height:219px;background:#fff;border-radius:8px;box-shadow:0 4px 24px rgba(30,40,80,.06);text-align:center;padding-top:17px}
.stars{color:#f39b1d;font-size:12px;letter-spacing:2px}
.tcard p{font-size:10.5px;line-height:18px;color:#9aa0ab;width:258px;margin:8px auto 0}
.avatar{width:36px;height:36px;border-radius:50%;margin:14px auto 0;background:linear-gradient(135deg,#c9ccd3,#7c818c)}
.tcard h5{font-size:12.5px;font-weight:500;margin-top:10px}
.dots{left:580px;top:2893px;display:flex;gap:4px}
.dots i{width:6px;height:6px;border-radius:50%;border:1px solid var(--red);display:block}
.dots i:first-child{background:var(--red)}

/* footer */
.f-head{font-size:15px;font-weight:500}
.f-links{list-style:none;font-size:11px;color:#666}
.f-links li{height:26.5px}
.soc{top:4119px;width:22px;height:22px;border-radius:50%;border:1.5px solid var(--blue)}
</style>
</head>
<body>

<header>
  <div class="abs logo" style="left:120px;top:23px">TAVORLY</div>
  <a class="abs nav-link" style="left:412px" href="#">What went well</a>
  <a class="abs nav-link" style="left:560px" href="#">What Didn't Go Well</a>
  <a class="abs nav-link" style="left:717px" href="#">Things To Try</a>
  <a class="abs nav-link" style="left:819px" href="#">Our Feature</a>
  <svg class="abs" style="left:905px;top:24px" width="20" height="24" viewBox="0 0 20 24" fill="none" stroke="#111827" stroke-width="1.6"><circle cx="10" cy="7" r="5"/><path d="M2 23c0-5 3.6-8 8-8s8 3 8 8z"/></svg>
  <a class="abs btn-dark" style="left:952px;top:20px;width:123px;height:34px" href="#">Let's Started</a>
</header>

<section>
  <h1 class="abs hero-title">Reflect, Learn, <span class="blue">Grow with</span><br>Structured <span class="mark y">Journaling</span></h1>
  <p class="abs hero-sub">Organize your thoughts and take actionable steps to improve your daily life.<br>A structured approach to journaling with actionable insights to help you improve.</p>
  <a class="abs btn-outline" href="#">Our Feature</a>

  <div class="abs dash">
    <aside class="abs dash-side">
      <div class="logo">TAVORLY</div>
      <div class="side-active"><i></i>Dashboard</div>
      <div class="side-item" style="top:118px"><i></i>Default Journal</div>
      <div class="side-item" style="top:154px"><i></i>Gym</div>
      <div class="side-item" style="top:184px"><i></i>Personal</div>
      <div class="side-item" style="top:220px"><i></i>Work</div>
      <div class="logout">Log Out
        <svg width="16" height="16" viewBox="0 0 16 16" fill="none" stroke="#2f7ff5" stroke-width="1.5"><path d="M12 4.5A6 6 0 1 0 12 11.5"/><path d="M7 8h8M12.5 5.5 15 8l-2.5 2.5"/></svg>
      </div>
    </aside>
    <div class="abs dash-hello">Hello Users !</div>
    <div class="abs dash-welcome">Welcome To Tavorly</div>
    <div class="abs bell"><svg width="16" height="16" viewBox="0 0 16 16" fill="none" stroke="#2f7ff5" stroke-width="1.4"><path d="M4 11V7a4 4 0 0 1 8 0v4l1.5 1.5h-11z"/><path d="M6.5 14h3"/></svg></div>
    <div class="abs dash-panel">
      <div class="abs jcard" style="left:19px"><div class="ic" role="img" aria-label="Journal icon" style="background:#fdf1e1"></div><span>Default Journal</span></div>
      <div class="abs jcard" style="left:169px"><div class="ic" role="img" aria-label="Gym icon" style="background:#e6f6ee"></div><span>Gym</span></div>
      <div class="abs jcard" style="left:320px"><div class="ic" role="img" aria-label="Personal icon" style="background:#fde8e6"></div><span>Personal</span></div>
      <div class="abs jcard" style="left:471px"><div class="ic" role="img" aria-label="Work icon" style="background:#fdf1e1"></div><span>Work</span></div>
      <a class="abs btn-dark btn-create" href="#">Create Project +</a>
      <div class="abs entry" style="left:20px">
        <b>Thu Aug 22 2024</b><span class="tag">What Went Well</span><br>
        Completed all scheduled workouts this week.<br>Increased bench press weight by 10 pounds.<br>Maintained consistent energy levels throughout sessions.<br>
        <span class="tag">What Didn't Go Well</span><br>Struggled with form on deadlifts, leading to lower back discomfort.
      </div>
      <div class="abs entry" style="left:302px">
        <b>Thu Aug 22 2024</b><span class="tag">What Went Well</span><br>
        Completed all scheduled workouts this week.<br>Increased bench press weight by 10 pounds.<br>Maintained consistent energy levels throughout sessions.<br>
        <span class="tag">What Didn't Go Well</span><br>Struggled with form on deadlifts, leading to lower back discomfort.
      </div>
    </div>
  </div>
</section>

<section>
  <h2 class="abs sec-title" style="top:920px"><span class="mark b">Journal Entry</span> Is&nbsp; Based<br>On&nbsp; <span class="red">Retrospective Board</span></h2>
  <p class="abs sec-desc" style="top:1036px">The focus will be on how the AI analyzes the user's entries across the three sections—"What Went Well,"<br>"What Didn't Go Well," and "Things to Try"—to offer meaningful guidance.</p>

  <div class="abs art" role="img" aria-label="Illustration of people reviewing progress charts" style="left:181px;top:1145px;width:445px;height:341px;background:linear-gradient(180deg,#ffffff 0%,#e9f7f0 60%,#1fae6a 92%)"></div>
  <div class="abs mini" style="left:124px;top:1203px;width:173px;height:173px">
    <div class="hd">What Went Well?</div>
    <div class="ed"><div class="tb">Normal B I U S</div>• Completed all scheduled workouts this week.<br>• Increased bench press weight by 10 pounds.<br>• Maintained consistent energy levels throughout sessions.</div>
  </div>
  <div class="abs eyebrow" style="left:680px;top:1121px;color:var(--green)">How It Leverages The Retrospective Board</div>
  <h3 class="abs feat-h" style="left:680px;top:1139px">What Went <span class="mark g">Well</span></h3>
  <p class="abs para" style="left:680px;top:1187px">Lorem Ipsum is simply dummy text of the printing and typesetting industry. Lorem Ipsum has been the industry's standard dummy text ever since the 1500s, when an unknown printer took a galley of type and scrambled it to make a type specimen book. It has survived not only five centuries, but also the leap into electronic typesetting, remaining essentially unchanged. It was popularised in the 1960s with the release of Letterform sheets containing Lorem Ipsum passages, and more recently with desktop publishing software like Pagewright including versions of Lorem Ipsum.</p>
  <div class="abs kf" style="left:680px;top:1347px;color:var(--green)">Key Features :</div>
  <ul class="abs checks" style="left:680px;top:1385px;width:345px">
    <li>Completed All Scheduled Workouts This Week.</li>
    <li>Increased Bench Press Weight By 10 Pounds.</li>
    <li>Maintained Consistent Energy Levels Throughout Sessions.</li>
  </ul>

  <div class="abs eyebrow" style="left:142px;top:1592px;color:var(--blue)">How It Leverages The Retrospective Board</div>
  <h3 class="abs feat-h" style="left:142px;top:1610px">What Didn't Go <span class="mark b">Well</span></h3>
  <p class="abs para" style="left:142px;top:1658px;width:370px">Lorem Ipsum is simply dummy text of the printing and typesetting industry. Lorem Ipsum has been the industry's standard dummy text ever since the 1500s, when an unknown printer took a galley of type and scrambled it to make a type specimen book. It has survived not only five centuries, but also the leap into electronic typesetting, remaining essentially unchanged.</p>
  <div class="abs kf" style="left:142px;top:1776px;color:var(--blue)">Key Features :</div>
  <ul class="abs checks" style="left:142px;top:1815px;width:345px">
    <li>Struggled With Form On Deadlifts, Leading To Lower Back Discomfort.</li>
    <li>Missed Two Stretching Sessions After Workouts.</li>
    <li>Skipped Meal Prep, Resulting In Inconsistent Nutrition.</li>
  </ul>
  <div class="abs art" role="img" aria-label="Illustration of two people exercising at home" style="left:545px;top:1612px;width:439px;height:346px;background:linear-gradient(180deg,#c7dcfb 0%,#e3ecfb 55%,#2f7ff5 78%)"></div>
  <div class="abs mini" style="left:915px;top:1656px;width:156px;height:170px">
    <div class="hd">What Didn't Go Well?</div>
    <div class="ed"><div class="tb">Normal B I U S</div>• Struggled with form on deadlifts, leading to lower back discomfort.<br>• Missed two stretching sessions after workouts.<br>• Skipped meal prep, resulting in inconsistent nutrition.</div>
  </div>

  <div class="abs art" role="img" aria-label="Illustration of two people preparing healthy meals" style="left:125px;top:2065px;width:439px;height:346px;background:linear-gradient(180deg,#fdf3e8 0%,#fbe6d2 62%,#e8473b 76%)"></div>
  <div class="abs mini" style="left:494px;top:2101px;width:165px;height:157px">
    <div class="hd">Things To Try</div>
    <div class="ed"><div class="tb">Normal B I U S</div>• Focus on deadlift form by lowering the weight and reviewing proper technique.<br>• Set reminders for post-workout stretching.<br>• Dedicate Sunday evenings to meal prep.</div>
  </div>
  <div class="abs eyebrow" style="left:680px;top:2044px;color:var(--red)">How It Leverages The Retrospective Board</div>
  <h3 class="abs feat-h" style="left:680px;top:2062px">Things To <span class="mark r">Try</span></h3>
  <p class="abs para" style="left:680px;top:2110px">Lorem Ipsum is simply dummy text of the printing and typesetting industry. Lorem Ipsum has been the industry's standard dummy text ever since the 1500s, when an unknown printer took a galley of type and scrambled it to make a type specimen book. It has survived not only five centuries, but also the leap into electronic typesetting, remaining essentially unchanged.</p>
  <div class="abs kf" style="left:680px;top:2228px;color:var(--red)">Key Features :</div>
  <ul class="abs checks" style="left:680px;top:2267px;width:360px">
    <li>Focus On&nbsp; Deadlift Form By Lowering The Weight And Reviewing Proper Technique.</li>
    <li>Set Reminders For Post-Workout Stretching To Prevent Muscle Tightness.</li>
    <li>Dedicate Sunday Evenings To Meal Prep To Ensure A Balanced.</li>
  </ul>
</section>

<section>
  <h2 class="abs sec-title" style="top:2506px;font-size:31px">WHAT <span class="mark g">CUSTOMERS SAY</span></h2>
  <p class="abs sec-desc" style="top:2564px">Lorem Ipsum is simply dummy text of the printing and typesetting industry. Lorem Ipsum has been<br>the industry's standard dummy text ever since the 1500s, when an unknown printer took a galley of<br>type and scrambled it to make a type specimen book.</p>
  <div class="abs tcard" style="left:124px"><div class="stars">★★★★★</div><p>Lorem Ipsum has been the industry's standard dummy text ever since the 1500s, when an unknown printer took a galley of type and scrambled it to make a type specimen book.</p><div class="avatar" role="img" aria-label="Customer portrait"></div><h5>Mara Ellison</h5></div>
  <div class="abs tcard" style="left:447px"><div class="stars">★★★★★</div><p>Lorem Ipsum has been the industry's standard dummy text ever since the 1500s, when an unknown printer took a galley of type and scrambled it to make a type specimen book.</p><div class="avatar" role="img" aria-label="Customer portrait"></div><h5>Mara Ellison</h5></div>
  <div class="abs tcard" style="left:769px"><div class="stars">★★★★★</div><p>Lorem Ipsum has been the industry's standard dummy text ever since the 1500s, when an unknown printer took a galley of type and scrambled it to make a type specimen book.</p><div class="avatar" role="img" aria-label="Customer portrait"></div><h5>Mara Ellison</h5></div>
  <div class="abs dots"><i></i><i></i><i></i><i></i></div>
</section>

<section>
  <h2 class="abs sec-title" style="top:2966px;font-size:31px">Features <span class="mark y">Products</span></h2>
  <p class="abs sec-desc" style="top:3024px">Lorem ipsum has been the industry's standard dummy text ever since the 1500s, when an unknown<br>printer took a galley of type and scrambled it to make a type specimen book.</p>

  <div class="abs" style="left:125px;top:3128px;font-size:12px;letter-spacing:.5px;color:#555">LOREM IPSUM IS SIMPLY DUMMY TEXT.</div>
  <h3 class="abs" style="left:125px;top:3158px;font-size:31px;font-weight:700;line-height:43px">Meet Your<br>Personal <span class="mark circ">AI Coach</span></h3>
  <p class="abs" style="left:125px;top:3265px;width:355px;font-size:10.8px;line-height:20px;color:var(--text)">Lorem Ipsum is simply dummy text of the printing and typesetting industry. Lorem Ipsum has been the industry's standard dummy text ever since the 1500s, when an unknown printer took a galley of type and scrambled it to make a type specimen book. It has survived not only five centuries, but also the leap into electronic typesetting, remaining essentially unchanged. It was popularised in the 1960s with the release of Letterform sheets containing Lorem Ipsum passages, and more recently with desktop publishing software like Pagewright including versions of Lorem Ipsum.</p>
  <div class="abs" style="left:125px;top:3461px;font-size:19px;font-weight:500">Key Features :</div>
  <ul class="abs checks bl" style="left:125px;top:3502px;width:380px">
    <li style="font-size:12.5px;margin-bottom:13px;font-weight:500">Lorem Ipsum Is Simply Dummy Text Of The Printing.</li>
    <li style="font-size:12.5px;margin-bottom:13px;font-weight:500">Text Of The Printing And Typesetting Industry.</li>
    <li style="font-size:12.5px;margin-bottom:13px;font-weight:500">AI Updates Deals In The CRM By Stage &amp; Context</li>
  </ul>
  <a class="abs btn-dark" style="left:127px;top:3617px;width:122px;height:37px;font-size:10.5px" href="#">Get In Touch</a>

  <div class="abs" style="left:552px;top:3139px;width:523px;height:421px;border-radius:14px;background:linear-gradient(180deg,#fffbec 0%,#fff7d8 60%,#fbe27a 60%,#f9dd6a 100%)"></div>
  <div class="abs" role="img" aria-label="App shown on a laptop and phone with journal entries" style="left:515px;top:3290px;width:510px;height:300px;border-radius:10px;background:linear-gradient(160deg,#3a3d44 0%,#1d1f24 100%);opacity:.9"></div>
</section>

<section>
  <div class="abs" style="left:0;width:1200px;top:3743px;text-align:center;font-size:12px;letter-spacing:.5px;color:var(--red)">SUBSCRIBE NOW</div>
  <h2 class="abs sec-title" style="top:3770px;font-size:31px">Join Our <span class="mark b">Community Today</span></h2>
  <p class="abs sec-desc" style="top:3843px">Don't miss out on the latest features and personalized advice—subscribe now!</p>
  <div class="abs" style="left:374px;top:3889px;width:315px;height:38px;border:1px solid var(--line);border-radius:5px;background:#fff;font-size:9.5px;color:#888;padding:12px 16px">Enter Your Email</div>
  <a class="abs btn-dark" style="left:700px;top:3889px;width:124px;height:38px;font-size:10.5px" href="#">Subscribe</a>
  <div class="abs" role="img" aria-label="Hand-drawn arrow pointing to the subscribe button" style="left:850px;top:3815px;width:85px;height:110px;border-radius:40px;background:rgba(232,71,59,.06)"></div>
</section>

<footer>
  <div class="abs logo" style="left:122px;top:4006px">TAVORLY</div>
  <p class="abs" style="left:122px;top:4049px;font-size:10.5px;line-height:20px;color:#555">Lorem Ipsum is simply dummy text of<br>the printing and typesetting industry.</p>
  <span class="abs soc" style="left:124px"></span>
  <span class="abs soc" style="left:155px"></span>
  <span class="abs soc" style="left:187px"></span>
  <span class="abs soc" style="left:218px"></span>

  <div class="abs f-head" style="left:575px;top:4006px">Quick Links</div>
  <ul class="abs f-links" style="left:575px;top:4034px"><li>What went well</li><li>What Didn't Go Well</li><li>Things To Try</li><li>Feature AI Coach</li></ul>
  <div class="abs f-head" style="left:788px;top:4006px">Social Media</div>
  <ul class="abs f-links" style="left:788px;top:4034px"><li>Facelink</li><li>Chirpnet</li><li>Snapgrid</li><li>Worknest</li></ul>
  <div class="abs f-head" style="left:985px;top:4006px">Support</div>
  <ul class="abs f-links" style="left:985px;top:4037px"><li style="height:24px">Terms &amp; services</li><li style="height:24px">Privacy Policy</li><li>Contact Us</li></ul>

  <div class="abs" style="left:122px;top:4186px;width:953px;height:1px;background:var(--line)"></div>
  <div class="abs" style="left:0;width:1200px;top:4212px;text-align:center;font-size:10px;color:#555">© Copyright All Right Reserved. Layoutfield Studio 2024.</div>
</footer>

</body>
</html>
```